Creative Landscape Architecture Company Needs a Creative Business Card Design

Marsh and Partners, Inc. is a landscape architecture (LA) company started in 1997 in Austin, TX. We work on large commerical projects all around the U.S. and provide land planning, site planning, landscape design and architectural renderings.

We don't want this card to look like a LA firm's business card. We are looking for a business card design that is edgy and cool to reflect the more artistic and creative side of our company. We would like our clients to think "now there's a business card unlike any other LA that I've seen before."

We would like it to be in standard 2"x3.5" format. Double sided. Full color ok. Our company logo is attached. We like the logo but would not be adverse to any variations you would like to make to it. Feel free to change it up. Typically the logo has been a light saturated orange color but its not necessary that you stick with it.

Requirements
Must have
• 1. Company name
2. individuals name
3. email address
4. cell number
5. office number
6. website: www.marshandpartners-demo.net
7. Business address
Nice to have
• Can add (but not necessary)
Personal titles such as "president" or "registered landscape architect"

```html
<!DOCTYPE html>
<html lang="en">
<head>
<meta charset="utf-8">
<title>Marsh and Partners, Inc. — Business Card</title>
<link rel="stylesheet" href="https://fonts.googleapis.com/css2?family=PT+Sans:wght@400;700&display=swap">
<style>
  :root {
    --canvas: #ffffff;
    --card-blue: #67acd6;
    --slate: #4a4b4d;
    --leaf-light: #8fc3ea;
    --leaf-deep: #1f6e9b;
    --ink-navy: #1d3550;
    --text-white: #ffffff;
  }
  * { box-sizing: border-box; margin: 0; padding: 0; }
  html, body {
    width: 1200px; height: 900px; overflow: hidden;
    background: var(--canvas);
    font-family: "PT Sans", "Myriad Pro", Arial, sans-serif;
  }
  .canvas { position: relative; width: 1200px; height: 900px; }
  .card {
    position: absolute; left: 372px; width: 456px; height: 261px;
    background: var(--card-blue); overflow: hidden;
  }
  .card--front { top: 147px; }
  .card--back { top: 491px; }

  /* front */
  .front__slate-column { position: absolute; left: 0; top: 0; width: 182px; height: 261px; background: var(--slate); }
  .front__slate-top { position: absolute; left: 0; top: 0; width: 273px; height: 60px; background: var(--slate); }
  .front__emblem {
    position: absolute; left: 182px; top: 60px; width: 91px; height: 141px;
    background: linear-gradient(90deg, #111 0%, #111 40%, var(--leaf-deep) 60%, var(--leaf-deep) 100%);
  }
  .front__company {
    position: absolute; left: 288px; top: 183px;
    color: var(--text-white); font-size: 14.5px; line-height: 18px; letter-spacing: -0.1px;
  }

  /* back */
  .back__foliage { position: absolute; left: 0; top: 0; width: 456px; height: 261px; }
  .back__name {
    position: absolute; left: 253px; top: 46px;
    color: var(--text-white); font-size: 14.5px; line-height: 18px;
  }
  .back__title {
    position: absolute; left: 253px; width: 166px; top: 72px; text-align: right;
    color: var(--text-white); font-size: 7px; font-weight: 700; line-height: 9px;
  }
  .contact { position: absolute; left: 0; top: 106px; width: 456px; }
  .contact__row { display: flex; font-size: 12px; line-height: 15.5px; }
  .contact__row + .contact__group { margin-top: 0; }
  .contact__group { margin-bottom: 15px; }
  .contact__label {
    width: 245px; text-align: right; padding-right: 8px;
    color: var(--ink-navy); font-weight: 700;
  }
  .contact__value { color: var(--text-white); font-weight: 700; }
</style>
</head>
<body>
<div class="canvas">

  <section class="card card--front">
    <div class="front__slate-column"></div>
    <div class="front__slate-top"></div>
    <div class="front__emblem" role="img" aria-label="Ornamental acanthus leaf emblem in black and deep blue"></div>
    <p class="front__company">Marsh and Partners, Inc.</p>
  </section>

  <section class="card card--back">
    <svg class="back__foliage" viewBox="0 0 456 261" role="img" aria-label="Large decorative acanthus leaf in light blue with a slate curl at the top left">
      <defs>
        <linearGradient id="foliageTone" x1="0" y1="0" x2="1" y2="1">
          <stop offset="0" stop-color="#8fc3ea"/>
          <stop offset="1" stop-color="#80bbe4"/>
        </linearGradient>
      </defs>
      <path d="M0 0 H265 C250 30 235 50 225 80 C200 110 185 150 175 190 C150 220 110 245 85 261 H0 Z" fill="url(#foliageTone)"/>
      <path d="M0 0 H150 C150 50 120 80 0 92 Z" fill="var(--slate)"/>
    </svg>

    <p class="back__name">Fname Lname</p>
    <p class="back__title">[ marketing director ]</p>

    <div class="contact">
      <div class="contact__group">
        <div class="contact__row"><span class="contact__label">adress.</span><span class="contact__value">4410 Cedar Bend Road, Suite 120</span></div>
        <div class="contact__row"><span class="contact__label"></span><span class="contact__value">Austin, Texas 78700</span></div>
      </div>
      <div class="contact__group">
        <div class="contact__row"><span class="contact__label">off.number.</span><span class="contact__value">512.555.0148</span></div>
        <div class="contact__row"><span class="contact__label">c.ph.number.</span><span class="contact__value">512 555 0193</span></div>
      </div>
      <div class="contact__group">
        <div class="contact__row"><span class="contact__label">e-mail.</span><span class="contact__value">mymail@marshandpartners-demo.net</span></div>
        <div class="contact__row"><span class="contact__label">web.site.</span><span class="contact__value">www.marshandpartners-demo.net</span></div>
      </div>
    </div>
  </section>

</div>
</body>
</html>
```